Super urgent - business card design

I need to design a business card
on the front side the words "VORTAL CAPITAL" with the top half surrounded by a stylised cloud. Minimalist, navy blue font on white background, with the Vortal capital in embossing.

On the back contact details (avoid centered). I would rather have the details taking the 2/3rd on the right and having the logo on the left, but anyway not plain centered

Renato Lo Cascio
CEO e Fondatore

r.locascio@vortal-capital.example
+39.347.512.6084

Piazza Torcelli 7
20135 Milano

```html
<!DOCTYPE html>
<html lang="it">
<head>
<meta charset="utf-8">
<title>Vortal Capital – Biglietto da visita</title>
<link rel="stylesheet" href="https://fonts.googleapis.com/css2?family=Roboto:wght@400;500&family=Roboto+Condensed:wght@400&display=swap">
<style>
  :root {
    --bg-deep: #163c1b;
    --brand-green: #359b40;
    --paper: #ffffff;
    --ink: #4a4a4a;
    --ink-dark: #3c3c3c;
  }
  * { margin: 0; padding: 0; box-sizing: border-box; }
  html, body { width: 930px; height: 1200px; overflow: hidden; }
  body {
    background: var(--bg-deep);
    font-family: "Roboto", sans-serif;
    position: relative;
  }
  .card {
    position: absolute;
    left: 85px;
    width: 760px;
    height: 474px;
    overflow: hidden;
  }
  .card--front { top: 100px; background: var(--paper); }
  .card--back { top: 626px; background: var(--brand-green); }

  /* Wordmark */
  .wordmark {
    position: absolute;
    display: flex;
    align-items: center;
    gap: 16px;
    font-weight: 500;
  }
  .wordmark__square { width: 30px; height: 30px; flex: none; }
  .wordmark__text { line-height: 1; }
  .wordmark__name { display: block; font-size: 60px; letter-spacing: 0.5px; }
  .wordmark__sub { display: block; font-size: 34px; letter-spacing: 17px; margin-top: 10px; }

  .card--front .wordmark { right: 58px; top: 58px; color: var(--brand-green); }
  .card--front .wordmark__square { background: var(--brand-green); }

  .card--back .wordmark { left: 50%; top: 160px; transform: translateX(-50%); color: var(--paper); }
  .card--back .wordmark__square { background: var(--paper); }

  /* Front details */
  .divider {
    position: absolute;
    left: 80px; right: 0; top: 258px;
    height: 2px;
    background: linear-gradient(90deg, rgba(53,155,64,0), rgba(53,155,64,0.45) 45%, var(--brand-green));
  }
  .person { position: absolute; left: 60px; top: 186px; }
  .person__name { font-size: 24px; font-weight: 500; color: var(--brand-green); letter-spacing: 0.3px; }
  .person__role { font-size: 17px; color: var(--ink-dark); margin-top: 4px; letter-spacing: 0.3px; }

  .address {
    position: absolute; left: 60px; top: 300px;
    font-size: 22px; line-height: 30px; color: var(--ink); letter-spacing: 0.6px;
    font-style: normal;
  }
  .contacts { position: absolute; left: 60px; top: 380px; list-style: none; color: var(--ink); }
  .contacts li { display: flex; align-items: center; gap: 10px; height: 28px; }
  .contacts svg { width: 20px; height: 18px; flex: none; }
  .contacts__phone { font-size: 22px; letter-spacing: 0.6px; }
  .contacts__mail { font-family: "Roboto Condensed", sans-serif; font-size: 22px; }

  .corner-band {
    position: absolute; right: 0; bottom: 0;
    width: 242px; height: 27px; background: var(--brand-green);
  }

  .website {
    position: absolute; left: 0; right: 0; bottom: 40px;
    text-align: center; color: var(--paper);
    font-size: 22px; letter-spacing: 3.6px;
  }
</style>
</head>
<body>

<section class="card card--front" aria-label="Fronte del biglietto">
  <div class="wordmark">
    <span class="wordmark__square"></span>
    <span class="wordmark__text">
      <span class="wordmark__name">VORTAL</span>
      <span class="wordmark__sub">CAPITAL</span>
    </span>
  </div>

  <div class="person">
    <p class="person__name">RENATO LO CASCIO</p>
    <p class="person__role">CEO E FONDATORE</p>
  </div>

  <div class="divider"></div>

  <address class="address">
    PIAZZA TORCELLI 7<br>
    20135 MILANO
  </address>

  <ul class="contacts">
    <li>
      <svg viewBox="0 0 24 24" aria-hidden="true"><path fill="#359b40" d="M6.6 10.8a15 15 0 0 0 6.6 6.6l2.2-2.2c.3-.3.7-.4 1-.2 1.1.4 2.3.6 3.6.6.6 0 1 .4 1 1V20c0 .6-.4 1-1 1A17 17 0 0 1 3 4c0-.6.4-1 1-1h3.5c.6 0 1 .4 1 1 0 1.3.2 2.5.6 3.6.1.3 0 .7-.2 1z"/></svg>
      <span class="contacts__phone">+39.347.512.6084</span>
    </li>
    <li>
      <svg viewBox="0 0 24 18" aria-hidden="true"><rect x="1" y="1" width="22" height="16" fill="#359b40"/><path d="M1 1l11 9 11-9M1 17l8-7M23 17l-8-7" fill="none" stroke="#fff" stroke-width="1.6"/></svg>
      <span class="contacts__mail">R.LOCASCIO@VORTAL-CAPITAL.EXAMPLE</span>
    </li>
  </ul>

  <div class="corner-band"></div>
</section>

<section class="card card--back" aria-label="Retro del biglietto">
  <div class="wordmark">
    <span class="wordmark__square"></span>
    <span class="wordmark__text">
      <span class="wordmark__name">VORTAL</span>
      <span class="wordmark__sub">CAPITAL</span>
    </span>
  </div>
  <p class="website">WWW.VORTALCAPITAL.EXAMPLE</p>
</section>

</body>
</html>
```